Poster of Insipirational Quotes

Attached is a list of leadership quotes from Arlen Drubeck. I would like a poster made, incorporating whatever design elements you like, potentially including Arlen's face, and one or more of the quotes. I intend to print this out in A3 or larger to hang on my wall.

The quotes are:

Being responsible sometimes means pissing people off.

The day soldiers stop bringing you their problems is the day you have stopped leading them.

Don't be buffaloed by experts and elites. Experts often possess more data than judgment. Elites can become so inbred that they produce hemophiliacs who bleed to death as soon as they are nicked by the real world.

Don't be afraid to challenge the pros, even in their own backyard.

Never neglect details. When everyone's mind is dulled or distracted the leader must be doubly vigilant.

You don't know what you can get away with until you try.

Keep looking below surface appearances. Don't shrink from doing so (just) because you might not like what you find.

Organization doesn't really accomplish anything. Plans don't accomplish anything, either. Theories of management don't much matter. Endeavors succeed or fail because of the people involved. Only by attracting the best people will you accomplish great deeds.

Organization charts and fancy titles count for next to nothing.

Never let your ego get so close to your position that when your position goes, your ego goes with it.

Fit no stereotypes. Don't chase the latest management fads. The situation dictates which approach best accomplishes the team's mission.

Perpetual optimism is a force multiplier.

Look for intelligence and judgment, and most critically, a capacity to anticipate, to see around corners. Also look for loyalty, integrity, a high energy drive, a balanced ego, and the drive to get things done.

Great leaders are almost always great simplifiers, who can cut through argument, debate and doubt, to offer a solution everybody can understand.

The commander in the field is always right and the rear echelon is wrong, unless proved otherwise.

Have fun in your command. Don't always run at a breakneck pace. Take leave when you've earned it: Spend time with your families. Corollary: surround yourself with people who take their work seriously, but not themselves, those who work hard and play hard.

Command is lonely.

Leadership is the art of accomplishing more than the science of management
says is possible.
Updates

I need to modify the specification based on the designs that I've seen.

Target Market(s)

Executive Office

Colors

Designer to choose colors to be used in the design.

Requirements
Must have
• Quotes

```html
<!DOCTYPE html>
<html lang="en">
<head>
<meta charset="utf-8">
<title>Leadership Quotes by Arlen Drubeck</title>
<link href="https://fonts.googleapis.com/css2?family=Lato:ital,wght@0,400;0,700;0,900;1,400;1,700&display=swap" rel="stylesheet">
<style>
  :root{
    --bg:#dfe0e5;
    --paper:#ffffff;
    --ink:#1a1a1a;
    --red:#8a0e0e;
    --blue-light:#5aa2ea;
    --blue-deep:#2b6cc4;
    --quote-blue:#3f8fe6;
    --rule:#111111;
  }
  *{margin:0;padding:0;box-sizing:border-box}
  html,body{width:1200px;height:1200px;overflow:hidden;background:var(--bg)}
  body{font-family:"Lato",sans-serif;color:var(--ink);position:relative}
  .poster{
    position:absolute;left:187px;top:16px;width:898px;height:1268px;
    background:var(--paper);transform:scale(.92);transform-origin:0 0;
    box-shadow:0 6px 18px rgba(0,0,0,.18);
  }
  .poster > *{position:absolute}
  .rule{background:var(--rule)}
  .line{background:#222}
  .header-band{left:0;top:0;width:436px;height:40px;background:var(--red);color:#fff;
    font-weight:700;font-size:18px;line-height:40px;padding-left:34px;letter-spacing:.2px}
  .qm{display:block}
  p{margin:0}
  .intro{left:114px;top:56px;width:742px;font-size:17.5px;line-height:23px;font-style:italic}
  .intro b{font-weight:700}
  .command{left:60px;top:174px;width:230px;text-align:center;font-weight:900;font-size:32px;line-height:34px}
  .command .underline{display:inline-block;border-bottom:4px solid var(--red);line-height:30px}
  .box{display:flex;align-items:center}
  .box-light{background:var(--blue-light)}
  .box-deep{background:var(--blue-deep);color:#fff}
  .box-red{background:var(--red);color:#fff}
  .challenge{left:321px;top:150px;width:262px;height:124px;padding:14px 34px 0 38px;
    font-size:21px;line-height:22.5px;text-align:justify;text-align-last:left;align-items:flex-start}
  .optimism{left:321px;top:289px;width:262px;height:124px;justify-content:center;text-align:center;
    font-weight:700;font-size:19px;line-height:26px;text-transform:uppercase}
  .get-away{left:615px;top:194px;width:225px;font-size:17.5px;line-height:21px;font-style:italic}
  .organization{left:53px;top:311px;width:236px;font-size:17px;line-height:21.8px;text-align:justify}
  .simplifiers{left:613px;top:298px;width:236px;font-size:15.8px;line-height:17.2px;text-align:justify}
  .ego{left:337px;top:470px;width:207px;font-size:15.5px;line-height:17.5px;font-style:italic;text-align:justify}
  .responsible{left:611px;top:454px;width:240px;text-align:center;font-size:20px;line-height:25px}
  .responsible b{font-weight:700;font-size:20.5px;text-transform:uppercase}
  .charts{left:45px;top:568px;width:262px;height:124px;justify-content:center;text-align:center;
    font-size:18px;line-height:22px;text-transform:uppercase;color:#111}
  .charts b{font-weight:700;border-bottom:3px solid var(--red)}
  .details{left:324px;top:568px;width:262px;height:124px;padding:0 18px 0 19px;
    font-size:16.3px;line-height:20.5px;text-align:justify;text-align-last:left;align-items:flex-start;padding-top:20px}
  .soldiers{left:610px;top:598px;width:245px;font-size:16.3px;line-height:17px;text-align:justify}
  .commander{left:61px;top:762px;width:218px;font-size:14.3px;line-height:18px;font-style:italic;text-align:justify}
  .stereotypes{left:345px;top:726px;width:226px;font-size:14.3px;line-height:18px;text-align:justify}
  .experts{left:615px;top:689px;width:238px;font-size:14.3px;line-height:18px;text-align:justify}
  .below{left:606px;top:835px;width:262px;height:104px;padding:8px 12px 0 12px;align-items:flex-start;
    font-size:16.3px;line-height:20.5px;font-style:italic;text-align:justify;text-align-last:left}
  .look-for{left:606px;top:951px;width:262px;height:144px;padding:8px 17px 0 14px;align-items:flex-start;
    font-size:14.3px;line-height:18px;text-align:justify;font-weight:700;color:#10203a}
  .look-for span{font-weight:400}
  .art{left:377px;top:886px;width:210px;font-size:18.5px;line-height:23px;font-style:italic}
  .art b{font-weight:700;text-transform:uppercase}
  .portrait{left:26px;top:856px}
  .signature{left:592px;top:1136px;width:272px;height:58px;border-radius:6px;
    background:linear-gradient(90deg,#ececec,#dadada)}
</style>
</head>
<body>
<main class="poster">
  <div class="header-band">LEADERSHIP QUOTES BY ARLEN DRUBECK</div>

  <!-- frame rules -->
  <div class="rule" style="left:448px;top:12px;width:437px;height:7px"></div>
  <div class="rule" style="left:877px;top:12px;width:8px;height:632px"></div>
  <div class="rule" style="left:17px;top:643px;width:8px;height:603px"></div>
  <div class="rule" style="left:17px;top:1238px;width:726px;height:8px"></div>

  <svg class="qm" style="left:33px;top:54px" width="58" height="46" viewBox="0 0 58 46" aria-hidden="true">
    <polygon fill="var(--quote-blue)" points="4,0 24,0 22,20 14,46 6,46 10,22 2,22"/>
    <polygon fill="var(--quote-blue)" points="34,0 56,0 54,20 46,46 38,46 42,22 32,22"/>
  </svg>
  <p class="intro"><b>Have fun in your command.</b> Don't always run at a breakneck pace. Take leave when you've earned it: Spend time with your families. Corollary: surround yourself with people who take their work seriously, but not themselves, those who work hard and play hard.</p>

  <!-- command is lonely -->
  <div class="line" style="left:193px;top:150px;width:111px;height:2px"></div>
  <div class="line" style="left:302px;top:150px;width:2px;height:24px"></div>
  <div class="line" style="left:43px;top:250px;width:2px;height:25px"></div>
  <div class="line" style="left:43px;top:273px;width:111px;height:2px"></div>
  <h2 class="command">COMMAND<br><span class="underline">IS LONELY</span></h2>

  <div class="box box-light challenge"><p><b>Don't be afraid</b> to challenge the pros, even in their own backyard.</p></div>
  <div class="box box-deep optimism"><p>Perpetual optimism is<br>a force multiplier</p></div>

  <!-- get away -->
  <div class="line" style="left:748px;top:150px;width:111px;height:2px"></div>
  <div class="line" style="left:857px;top:150px;width:2px;height:24px"></div>
  <svg class="qm" style="left:815px;top:158px" width="36" height="28" viewBox="0 0 36 28" aria-hidden="true">
    <polygon fill="var(--quote-blue)" points="2,0 15,0 15,12 10,28 4,28 7,14 2,14"/>
    <polygon fill="var(--quote-blue)" points="20,0 34,0 34,12 29,28 23,28 26,14 20,14"/>
  </svg>
  <p class="get-away">You don't know what you can get away with until you try.</p>
  <div class="line" style="left:598px;top:250px;width:2px;height:25px"></div>
  <div class="line" style="left:598px;top:273px;width:111px;height:2px"></div>

  <p class="organization">Organization doesn't really accomplish anything. Plans don't accomplish anything, either. Theories of management don't much matter. Endeavors succeed or fail because of the people involved. <b>Only by attracting the best people will you accomplish great deeds.</b></p>

  <p class="simplifiers"><b>Great leaders are almost always great simplifiers</b>, who can cut through argument, debate and doubt, to offer a solution everybody can understand.</p>

  <!-- ego -->
  <div class="line" style="left:475px;top:429px;width:111px;height:2px"></div>
  <div class="line" style="left:584px;top:429px;width:2px;height:24px"></div>
  <svg class="qm" style="left:543px;top:436px" width="36" height="28" viewBox="0 0 36 28" aria-hidden="true">
    <polygon fill="var(--quote-blue)" points="2,0 15,0 15,12 10,28 4,28 7,14 2,14"/>
    <polygon fill="var(--quote-blue)" points="20,0 34,0 34,12 29,28 23,28 26,14 20,14"/>
  </svg>
  <p class="ego"><b>Never let your ego get so close to your position</b> that when your position goes, your ego goes.</p>
  <div class="line" style="left:326px;top:532px;width:2px;height:19px"></div>

  <!-- responsible -->
  <div class="line" style="left:750px;top:429px;width:111px;height:2px"></div>
  <div class="line" style="left:859px;top:429px;width:2px;height:24px"></div>
  <p class="responsible"><b>Being responsible</b><br>sometimes means<br>pissing people off.</p>
  <div class="line" style="left:600px;top:528px;width:2px;height:24px"></div>
  <div class="line" style="left:600px;top:550px;width:111px;height:2px"></div>

  <div class="box box-light charts"><p>Organization charts<br>and fancy titles<br>count for next to<br><b>nothing</b></p></div>
  <div class="box box-red details"><p><b>Never neglect details.</b> When everyone's mind is dulled or distracted the leader must be doubly vigilant.</p></div>

  <p class="soldiers">The day soldiers stop bringing you their problems is the day you have stopped leading them.</p>

  <!-- commander -->
  <div class="line" style="left:196px;top:708px;width:111px;height:2px"></div>
  <div class="line" style="left:305px;top:708px;width:2px;height:24px"></div>
  <svg class="qm" style="left:263px;top:717px" width="36" height="28" viewBox="0 0 36 28" aria-hidden="true">
    <polygon fill="var(--quote-blue)" points="2,0 15,0 15,12 10,28 4,28 7,14 2,14"/>
    <polygon fill="var(--quote-blue)" points="20,0 34,0 34,12 29,28 23,28 26,14 20,14"/>
  </svg>
  <p class="commander">The commander in the field is always right and the rear echelon is wrong, unless proved otherwise.</p>
  <div class="line" style="left:46px;top:806px;width:2px;height:24px"></div>
  <div class="line" style="left:46px;top:828px;width:111px;height:2px"></div>

  <!-- stereotypes -->
  <div class="line" style="left:475px;top:708px;width:111px;height:2px"></div>
  <div class="line" style="left:584px;top:708px;width:2px;height:24px"></div>
  <p class="stereotypes"><b>Fit no stereotypes.</b> Don't chase the latest management fads. The situation dictates which approach best accomplishes the team's mission.</p>
  <div class="line" style="left:326px;top:806px;width:2px;height:24px"></div>
  <div class="line" style="left:326px;top:828px;width:111px;height:2px"></div>

  <p class="experts">Don't be buffaloed by experts and elites. Experts often possess more data than judgment. Elites can become so inbred that they produce hemophiliacs who bleed to death as soon as they are nicked by the real world.</p>

  <div class="box box-deep below"><p>Keep looking below surface appearances. Don't shrink from doing so (just) because you might not like what you find.</p></div>
  <div class="box box-light look-for"><p>Look for intelligence and judgement, <span>and most critically, a capacity to anticipate, to see around corners. Also look for</span> loyalty, integrity, a high energy drive, a balanced ego, and the drive to get things done.</p></div>

  <svg class="portrait" width="560" height="382" viewBox="0 0 560 382" role="img" aria-label="Grayscale portrait of Arlen Drubeck gesturing while speaking">
    <defs>
      <linearGradient id="portraitTone" x1="0" y1="0" x2="1" y2="1">
        <stop offset="0" stop-color="#bdbdbd"/>
        <stop offset=".55" stop-color="#7a7a7a"/>
        <stop offset="1" stop-color="#d6d6d6"/>
      </linearGradient>
    </defs>
    <path fill="url(#portraitTone)" d="M0,382 L0,200 L60,150 L110,30 L200,0 L300,40 L330,150 L420,200 L500,300 L560,382 Z"/>
  </svg>

  <svg class="qm" style="left:519px;top:861px" width="58" height="44" viewBox="0 0 58 44" aria-hidden="true">
    <polygon fill="var(--red)" points="2,0 24,0 24,18 16,44 6,44 11,20 2,20"/>
    <polygon fill="var(--red)" points="33,0 56,0 56,18 48,44 38,44 43,20 33,20"/>
  </svg>
  <p class="art"><b>Leadership is</b><br>the art of accomplishing more than the science of management says is possible.</p>

  <div class="signature" role="img" aria-label="Handwritten signature of Arlen Drubeck"></div>
</main>
</body>
</html>
```